Software Development Consulting Company Needs Business Card Design

We need a new business card design for our consultants at Verdant Systems (verdantsystems.example). We are a small firm that provides high-end software development and methodology consulting to medium to large enterprise IT organizations.

Our logo uses Futura for the font and we would like to stick with navy blue and canary yellow for the logo colors. Attached are normal and reversed versions of our logos in illustrator format.
Updates

Hi Everyone, Thank yo very much for your amazing design ideas. I have created a poll for this project and our employees will be voting on the design they wish to use. We will be making a decision this Wednesday (October 22nd). Thanks again, Marcus Hallward

Industry/Entity Type

Business

```html
<!DOCTYPE html>
<html lang="en">
<head>
<meta charset="utf-8">
<title>Verdant Systems – Business Card</title>
<link rel="stylesheet" href="https://fonts.googleapis.com/css2?family=Jost:wght@400;500&family=Lato:wght@400;700&display=swap">
<style>
  :root {
    --backdrop: #e6e6e6;
    --navy: #1f4467;
    --navy-deep: #15304e;
    --navy-light: #335d7d;
    --canary: #f5e11a;
    --paper: #f4f4f3;
    --ink: #2b2b2b;
    --white: #ffffff;
  }
  * { margin: 0; padding: 0; box-sizing: border-box; }
  html, body {
    width: 1200px;
    height: 720px;
    overflow: hidden;
    background: var(--backdrop);
  }
  .canvas {
    position: relative;
    width: 1200px;
    height: 720px;
  }
  .card {
    position: absolute;
    top: 242px;
    width: 420px;
    height: 240px;
    overflow: hidden;
  }
  /* Front */
  .card-front {
    left: 147px;
    background: var(--paper);
  }
  .front-band {
    position: absolute;
    left: 0; top: 0;
    width: 128px;
    height: 100%;
    background: var(--navy);
  }
  .wordmark {
    position: absolute;
    display: flex;
    align-items: center;
    gap: 8px;
    font-family: "Jost", sans-serif;
    font-weight: 500;
    text-transform: uppercase;
    white-space: nowrap;
  }
  .wordmark-dot {
    border-radius: 50%;
    background: var(--canary);
    flex: none;
  }
  .front-wordmark {
    right: 15px;
    top: 22px;
    font-size: 15px;
    letter-spacing: 3px;
    color: var(--navy);
  }
  .front-wordmark .wordmark-dot { width: 9px; height: 9px; }
  .contact {
    position: absolute;
    right: 15px;
    text-align: right;
    font-family: "Lato", sans-serif;
    color: var(--ink);
  }
  .person { top: 79px; }
  .person-name {
    font-weight: 700;
    font-size: 13.5px;
    color: var(--navy);
    letter-spacing: -0.2px;
  }
  .person-title {
    font-size: 10px;
    margin-top: 1px;
  }
  .details {
    top: 120px;
    list-style: none;
    font-size: 9.6px;
    line-height: 12px;
  }
  .details li {
    display: flex;
    justify-content: flex-end;
    align-items: center;
    gap: 6px;
  }
  .details svg { width: 10px; height: 10px; flex: none; }
  .address {
    right: 17px;
    top: 197px;
    font-size: 9.6px;
    line-height: 12px;
  }
  /* Back */
  .card-back {
    left: 633px;
    background: linear-gradient(160deg, var(--navy-light) 0%, var(--navy) 50%, var(--navy-deep) 100%);
  }
  .back-wordmark {
    left: 50%;
    top: 50%;
    transform: translate(-50%, -50%);
    font-size: 25px;
    letter-spacing: 6px;
    color: var(--white);
    gap: 12px;
  }
  .back-wordmark .wordmark-dot { width: 12px; height: 12px; }
</style>
</head>
<body>
<main class="canvas">

  <section class="card card-front" aria-label="Business card front">
    <div class="front-band"></div>

    <div class="wordmark front-wordmark">
      <span class="wordmark-dot"></span>
      <span>Verdant Systems</span>
    </div>

    <div class="contact person">
      <p class="person-name">Marcus Hallward</p>
      <p class="person-title">Principal Consultant</p>
    </div>

    <ul class="contact details">
      <li>555-014-2290
        <svg viewBox="0 0 10 10" aria-hidden="true"><path d="M1 4 Q5 0 9 4 L8 5 L6.5 4 L6.5 3.3 Q5 2.8 3.5 3.3 L3.5 4 L2 5 Z M2.5 5.5 H7.5 L8.5 9 H1.5 Z" fill="var(--navy)"/></svg>
      </li>
      <li>marcus.hallward@verdantsystems.example
        <svg viewBox="0 0 10 10" aria-hidden="true"><rect x="0.5" y="2" width="9" height="6.5" fill="var(--navy)"/><path d="M0.8 2.4 L5 6 L9.2 2.4" stroke="var(--white)" stroke-width="0.8" fill="none"/></svg>
      </li>
      <li>@mhallward
        <svg viewBox="0 0 10 10" aria-hidden="true"><rect x="0.5" y="1.5" width="9" height="6" fill="none" stroke="var(--navy)" stroke-width="1.2"/><rect x="3" y="8.3" width="4" height="1.2" fill="var(--navy)"/></svg>
      </li>
      <li>www.verdantsystems.example
        <svg viewBox="0 0 10 10" aria-hidden="true"><rect x="0.5" y="0.5" width="9" height="9" rx="1.5" fill="var(--navy)"/></svg>
      </li>
    </ul>

    <address class="contact address" style="font-style: normal;">
      4471 Larkspur Office Pkwy,<br>
      Fairview, MO 65010
    </address>
  </section>

  <section class="card card-back" aria-label="Business card back">
    <div class="wordmark back-wordmark">
      <span class="wordmark-dot"></span>
      <span>Verdant Systems</span>
    </div>
  </section>

</main>
</body>
</html>
```